business card double side design

We need a business card design for our company BRIGHTlearn. DOUBLE SIDED. We provide continuing education programs & courses across North America. Our website is www.brightlearn-example.com - please use the grey pinstrip concept as part of the design. Compliment the branding that is occuring on that site!
Please use pantones daa520 and 3f3151. Verdana for text. I have attached our logo.
I would like the logo & website address www.BRIGHTlearn-example.com on the front of the card, all other info on the backside. The final design should communicate authority and credibility.

Industry/Entity Type

Professional Service

Font styles to use
Other font styles liked:
• verdanda

Requirements
Must have
• pantones daa520 and 3f3151. Verdana for text.
• must compliment the branding occuring on the www.BRIGHTlearn-example.com

```html
<!DOCTYPE html>
<html lang="en">
<head>
<meta charset="utf-8">
<title>BRIGHTlearn Business Card</title>
<link href="https://fonts.googleapis.com/css2?family=Inter:wght@400;700&display=swap" rel="stylesheet">
<style>
  :root {
    --gold: #daa520;
    --purple: #3f3151;
    --charcoal: #333132;
    --stripe-light: #f7f7f8;
    --stripe-mid: #e8e9eb;
    --shadow: #d6d6d6;
    --border: #dcdcdc;
    --url-grey: #6a6a6a;
    --label: #4a5530;
    --white: #ffffff;
  }
  html, body {
    margin: 0;
    padding: 0;
    width: 1200px;
    height: 901px;
    overflow: hidden;
    background: var(--white);
    font-family: Verdana, "DejaVu Sans", Inter, sans-serif;
  }
  .canvas { position: relative; width: 1200px; height: 901px; }

  .card {
    position: absolute;
    width: 593px;
    box-sizing: border-box;
    border: 1px solid var(--border);
    box-shadow: 8px 8px 0 var(--shadow);
    overflow: hidden;
  }
  .card--front { left: 298px; top: 60px; height: 365px; background: var(--white); }
  .card--back  { left: 297px; top: 475px; height: 363px; background: var(--purple); }

  .band { position: absolute; left: 0; right: 0; }
  .band--purple { top: 0; height: 33px; background: var(--purple); }
  .band--gold { height: 8px; background: var(--gold); }
  .band--charcoal { bottom: 0; background: var(--charcoal); }

  .pinstripe {
    position: absolute; left: 0; right: 0; top: 41px; height: 280px;
    background:
      repeating-linear-gradient(90deg,
        var(--stripe-light) 0px, var(--stripe-mid) 14px,
        var(--stripe-light) 30px);
  }

  .brand {
    position: absolute; left: 108px; top: 88px;
    display: flex; align-items: center; gap: 22px;
  }
  .brand__mark { width: 128px; height: 128px; border-radius: 50%; background: var(--gold); }
  .brand__name {
    font-weight: 700; font-size: 32px; color: var(--gold); letter-spacing: 0.5px;
  }

  .card__url {
    position: absolute; left: 0; right: 0; top: 281px;
    text-align: center; font-size: 19px; letter-spacing: 0.4px; color: var(--url-grey);
  }

  .contact { position: absolute; left: 0; right: 0; text-align: center; letter-spacing: 0.4px; }
  .contact--person { top: 78px; color: var(--gold); }
  .contact__name { font-weight: 700; font-size: 19px; line-height: 23px; }
  .contact__title { font-size: 19px; line-height: 23px; }
  .contact--office { top: 196px; color: var(--white); font-size: 18px; line-height: 21px; }
  .contact__office-title { font-weight: 700; font-size: 19px; }

  .side-label {
    position: absolute; left: 916px; font-size: 18px; color: var(--label);
  }
</style>
</head>
<body>
<div class="canvas">

  <section class="card card--front" aria-label="Card front">
    <div class="band band--purple"></div>
    <div class="band band--gold" style="top:33px"></div>
    <div class="pinstripe"></div>
    <div class="band band--gold" style="top:321px"></div>
    <div class="band band--charcoal" style="height:35px"></div>

    <div class="brand">
      <div class="brand__mark"></div>
      <div class="brand__name">BRIGHTlearn</div>
    </div>
    <div class="card__url">www.BRIGHTlearn-example.com</div>
  </section>
  <div class="side-label" style="top:410px">front</div>

  <section class="card card--back" aria-label="Card back">
    <div class="contact contact--person">
      <div class="contact__name">Daniel Hartwell</div>
      <div class="contact__title">Technical Consultant</div>
    </div>
    <div class="contact contact--office">
      <div class="contact__office-title">Canada Headquarters</div>
      <div>Suite 140, 52 Maplewood Avenue</div>
      <div>Red Deer, AB. T4N 2K7</div>
      <div>Tel: (403) 555-0187</div>
      <div>Email: support@BRIGHTlearn-example.com</div>
    </div>
    <div class="band band--gold" style="top:319px"></div>
    <div class="band band--charcoal" style="height:35px"></div>
  </section>
  <div class="side-label" style="top:825px">back</div>

</div>
</body>
</html>
```